New Board Game - KZ 45:35:20

The project is in two phases:
A. GAME BOARD DESIGN
Design of a striking game board.
NB. See the following files:
* KZ 45:35:20 Background Info
* KZ 45:35:20 Game Board Format
NB. The contest fee is for Phase A only. Additional fees will be paid for Phase B.
B. APPLICATION OF GAME BOARD DESIGN
The game board design will to be applied to the following game materials:
* Game cards (front and back)
* Sticker for game board tube
* Facilitator's Handbook front and back cover
* Icon for pages inside Facilitator's Handbook
Additional information on the game cards will be provided to the winning designer.
Updates
Please note that the project fee is for Phase A only. We will pay additional fees for Phase B, i.e. game cards etc.
NOTE:
Please keep in mind that the game will be used in a corporate setting. The initial target group are Learning and Development (L&D) specialists, mainly people who develop or deliver training courses. They are all educated professionals.
I recently included this feedback in a message to one of the designers:
The game board has to have a level of sophistication and elegance that suits a corporate environment. The game will also be the first direct contact that some potential members will have with the Guild and has to make a positive impression on them.
We want people to perceive the game as a top-class, creative product.
PLEASE NOTE:
The project fee is now a guaranteed payment.
Target Market(s)
The game will initially be used at networking events held by the Halvern Guild of Practitioners in Australia (see: www.halverncircle.example). These events are attended by members and guests, with the group ranging from 10 to 20 attendees.
The game may also be used as part of management or leadership development programs in business and government organisations.
Another possible use is with teachers at networking events or professional development courses.
Requirements
Must have
- See the uploaded files for important design requirements.
What is most important is that the game materials are attractive, appealing, impactful. People (in the target group) who see the game materials should feel that they want to find out more, pick up the cards and play the game.
Should not have
- Still thinking....

```html
<!DOCTYPE html>
<html lang="en">
<head>
<meta charset="utf-8">
<title>KZ 45:35:20 – Game Board</title>
<link rel="stylesheet" href="https://fonts.googleapis.com/css2?family=Open+Sans:wght@600;700;800&family=Bangers&display=swap">
<style>
  :root {
    --page: #ffffff;
    --board-edge: #1b2f86;
    --field-light: #1aa3e0;
    --field-dark: #0d3d99;
    --tile-edge: #172a7a;
    --orange-top: #ffa12a;
    --orange-bottom: #f26a12;
    --green-top: #9be22a;
    --green-bottom: #54b414;
    --blue-top: #39c6ff;
    --blue-bottom: #0b86e0;
    --yellow-top: #ffd84a;
    --yellow-bottom: #f4b800;
    --corner-red: #d4151b;
    --corner-dark: #8e0b10;
    --burst-text: #f26a12;
    --white: #ffffff;
    --ink: #1c1c1c;
  }
  * { box-sizing: border-box; margin: 0; padding: 0; }
  html, body { width: 1200px; height: 900px; overflow: hidden; background: var(--page); }
  body { position: relative; font-family: "Open Sans", Arial, sans-serif; }

  .board {
    position: absolute; left: 183px; top: 44px; width: 864px; height: 721px;
    background: var(--board-edge); padding: 7px;
  }
  .board__field {
    position: absolute; inset: 7px;
    background: radial-gradient(ellipse at 20% 85%, var(--field-light) 0%, #0f6fc6 45%, var(--field-dark) 100%);
  }

  .tile {
    position: absolute; width: 68px; height: 72px;
    border: 3px solid var(--tile-edge); border-radius: 6px;
    display: flex; align-items: center; justify-content: center;
    color: var(--white); font-weight: 700; font-size: 26px; letter-spacing: -0.5px;
    box-shadow: inset 0 0 0 1px rgba(255,255,255,0.25);
  }
  .tile--side { width: 74px; height: 64px; }
  .tile sup { font-size: 9px; vertical-align: top; position: relative; top: 4px; margin-left: 1px; }
  .tile--seventy { background: linear-gradient(var(--orange-top), var(--orange-bottom)); }
  .tile--twenty { background: linear-gradient(var(--green-top), var(--green-bottom)); }
  .tile--ten { background: linear-gradient(var(--blue-top), var(--blue-bottom)); }
  .tile--action { background: linear-gradient(var(--yellow-top), var(--yellow-bottom)); }
  .action-badge {
    width: 46px; height: 46px; border: 2px solid var(--ink); border-radius: 50%;
    display: flex; align-items: center; justify-content: center; text-align: center;
    color: var(--ink); font-size: 11px; line-height: 1.05; font-weight: 700;
  }
  .tile__face { display: inline-flex; align-items: center; justify-content: center; }
  .tile__face--down { transform: rotate(180deg); }
  .tile__face--left { transform: rotate(90deg); }
  .tile__face--right { transform: rotate(-90deg); }

  .corner { position: absolute; width: 156px; height: 152px; }
  .corner--tl { left: 24px; top: 24px; }
  .corner--tr { right: 24px; top: 24px; transform: scaleX(-1); }
  .corner--bl { left: 24px; bottom: 24px; transform: scaleY(-1); }
  .corner--br { right: 24px; bottom: 24px; transform: scale(-1,-1); }
  .corner-word {
    position: absolute; font-family: "Bangers", Impact, sans-serif;
    font-size: 30px; color: var(--burst-text); letter-spacing: 1px;
    background: var(--white); padding: 2px 8px; border-radius: 14px;
  }
  .corner-word--tl { left: 34px; top: 80px; transform: rotate(135deg); }
  .corner-word--tr { right: 38px; top: 78px; transform: rotate(-135deg); }
  .corner-word--bl { left: 38px; bottom: 80px; transform: rotate(45deg); }
  .corner-word--br { right: 32px; bottom: 80px; transform: rotate(-45deg); }

  .copyright {
    position: absolute; font-size: 6.5px; color: var(--white); white-space: nowrap; letter-spacing: 0.2px;
  }
  .copyright--bottom { left: 180px; top: 606px; }
  .copyright--top { left: 507px; top: 104px; transform: rotate(180deg); }

  .title {
    position: absolute; left: 0; right: 0; top: 300px; text-align: center;
    color: var(--white); font-weight: 800; font-size: 92px; letter-spacing: -2px; line-height: 1;
  }
</style>
</head>
<body>
<main class="board">
  <div class="board__field"></div>

  <!-- corners -->
  <svg class="corner corner--tl" viewBox="0 0 156 152" aria-hidden="true">
    <defs><linearGradient id="cornerFill" x1="0" y1="0" x2="1" y2="1"><stop offset="0" stop-color="#e8242a"/><stop offset="1" stop-color="#8e0b10"/></linearGradient></defs>
    <path d="M0 152 V88 A88 88 0 0 1 88 0 H156 V72 H112 A40 40 0 0 0 72 112 V152 Z" fill="url(#cornerFill)" stroke="#172a7a" stroke-width="3"/>
  </svg>
  <svg class="corner corner--tr" viewBox="0 0 156 152" aria-hidden="true"><path d="M0 152 V88 A88 88 0 0 1 88 0 H156 V72 H112 A40 40 0 0 0 72 112 V152 Z" fill="url(#cornerFill)" stroke="#172a7a" stroke-width="3"/></svg>
  <svg class="corner corner--bl" viewBox="0 0 156 152" aria-hidden="true"><path d="M0 152 V88 A88 88 0 0 1 88 0 H156 V72 H112 A40 40 0 0 0 72 112 V152 Z" fill="url(#cornerFill)" stroke="#172a7a" stroke-width="3"/></svg>
  <svg class="corner corner--br" viewBox="0 0 156 152" aria-hidden="true"><path d="M0 152 V88 A88 88 0 0 1 88 0 H156 V72 H112 A40 40 0 0 0 72 112 V152 Z" fill="url(#cornerFill)" stroke="#172a7a" stroke-width="3"/></svg>
  <span class="corner-word corner-word--tl">YIKES!</span>
  <span class="corner-word corner-word--tr">OOPS!</span>
  <span class="corner-word corner-word--bl">UH-OH!</span>
  <span class="corner-word corner-word--br">CRIKEY!</span>

  <!-- top row (faces the far player) -->
  <div class="tile tile--twenty" style="left:186px;top:24px"><span class="tile__face tile__face--down">35<sup>%</sup></span></div>
  <div class="tile tile--action" style="left:258px;top:24px"><span class="tile__face tile__face--down action-badge">ROLL<br>again</span></div>
  <div class="tile tile--seventy" style="left:330px;top:24px"><span class="tile__face tile__face--down">45<sup>%</sup></span></div>
  <div class="tile tile--seventy" style="left:402px;top:24px"><span class="tile__face tile__face--down">45<sup>%</sup></span></div>
  <div class="tile tile--seventy" style="left:474px;top:24px"><span class="tile__face tile__face--down">45<sup>%</sup></span></div>
  <div class="tile tile--action" style="left:546px;top:24px"><span class="tile__face tile__face--down action-badge">ANY<br>card</span></div>
  <div class="tile tile--ten" style="left:618px;top:24px"><span class="tile__face tile__face--down">20<sup>%</sup></span></div>

  <!-- left column -->
  <div class="tile tile--side tile--twenty" style="left:24px;top:186px"><span class="tile__face tile__face--left">35<sup>%</sup></span></div>
  <div class="tile tile--side tile--ten" style="left:24px;top:258px"><span class="tile__face tile__face--left">20<sup>%</sup></span></div>
  <div class="tile tile--side tile--action" style="left:24px;top:330px"><span class="tile__face tile__face--left action-badge">MISS<br>a turn</span></div>
  <div class="tile tile--side tile--seventy" style="left:24px;top:402px"><span class="tile__face tile__face--left">45<sup>%</sup></span></div>
  <div class="tile tile--side tile--seventy" style="left:24px;top:474px"><span class="tile__face tile__face--left">45<sup>%</sup></span></div>

  <!-- right column -->
  <div class="tile tile--side tile--twenty" style="left:766px;top:186px"><span class="tile__face tile__face--right">35<sup>%</sup></span></div>
  <div class="tile tile--side tile--twenty" style="left:766px;top:258px"><span class="tile__face tile__face--right">35<sup>%</sup></span></div>
  <div class="tile tile--side tile--action" style="left:766px;top:330px"><span class="tile__face tile__face--right action-badge">MISS<br>a turn</span></div>
  <div class="tile tile--side tile--seventy" style="left:766px;top:402px"><span class="tile__face tile__face--right">45<sup>%</sup></span></div>
  <div class="tile tile--side tile--seventy" style="left:766px;top:474px"><span class="tile__face tile__face--right">45<sup>%</sup></span></div>

  <!-- bottom row -->
  <div class="tile tile--seventy" style="left:186px;top:626px">45<sup>%</sup></div>
  <div class="tile tile--action" style="left:258px;top:626px"><span class="action-badge">ANY<br>card</span></div>
  <div class="tile tile--twenty" style="left:330px;top:626px">35<sup>%</sup></div>
  <div class="tile tile--twenty" style="left:402px;top:626px">35<sup>%</sup></div>
  <div class="tile tile--ten" style="left:474px;top:626px">20<sup>%</sup></div>
  <div class="tile tile--action" style="left:546px;top:626px"><span class="action-badge">ROLL<br>again</span></div>
  <div class="tile tile--seventy" style="left:618px;top:626px">45<sup>%</sup></div>

  <p class="copyright copyright--bottom">© Dana Morrow, Halvern Guild of Practitioners &nbsp;www.</p>
  <p class="copyright copyright--top">© Dana Morrow, Halvern Guild of Practitioners &nbsp;www.</p>

  <h1 class="title">KZ 45:35:20</h1>
</main>
</body>
</html>
```